Auto VS Manual Money War Postcard creation

This is a mail marketing campaign that helps people create wealth while learning about this industry. I am looking to have a postcard designed that will have truthful information according to the flyers added. It needs to be clear that the potential amount of money any one can make is on the postcard somewhere. It also should get the point across that they dont need to sell and even if they cant get a referral they will be able to make money.
The "postcard attachment" is something I was working on and is an example of how to get the message across without putting all the detail in. I dont like what I have created which is why I am reaching out.

Target Market(s)

Mail Marketing Opportunity seekers

Industry/Entity Type

Industry

Font styles to use
Sans Serif
Decorative

Colors

Designer to choose colors to be used in the design.

Requirements
Must have
• My project must have a place for people to put a referring member name in. It also must have that the cost is $5 to get started. It must be clear that there are two income streams that people will qualify for when they join for $5. It must have the amount of money that can potentially be made in this program.
Nice to have
• A similar header to what you see on the attached flyer. as much info that can tactfully fit within a standard postcard. my email address for questions and my name and address for them to return the postcard and money to.
Should not have
• Misspellings

```html
<!DOCTYPE html>
<html lang="en">
<head>
<meta charset="utf-8">
<title>Automatic vs Manual Money War – Postcard</title>
<link rel="stylesheet" href="https://fonts.googleapis.com/css2?family=Open+Sans:wght@400;600;700;800&family=Roboto+Condensed:wght@400;700&display=swap">
<style>
:root{
  --bg:#e9e7e3;
  --card:#ffffff;
  --red:#c0212f;
  --red-dark:#7d1019;
  --yellow:#ffd21f;
  --panel:#e6e7e8;
  --blue:#1e8fc4;
  --ink:#1f1f1f;
  --muted:#6d6e71;
}
*{box-sizing:border-box;margin:0;padding:0}
html,body{width:849px;height:1200px;overflow:hidden}
body{background:var(--bg);font-family:"Open Sans",Arial,sans-serif;color:var(--ink);position:relative}
.card{position:absolute;left:104px;width:637px;background:var(--card);box-shadow:0 4px 14px rgba(0,0,0,.25);overflow:hidden}
.card--front{top:71px;height:492px}
.card--back{top:605px;height:494px}

/* front */
.hero{position:absolute;left:0;top:0;width:100%;height:178px;
  background:linear-gradient(180deg,#c9ccce 0%,#b5ad86 45%,#8e8a55 75%,#6f6a3f 100%)}
.banner{position:absolute;left:29px;top:154px;width:290px;height:126px;background:var(--red);
  text-align:center;color:#fff;font-family:"Roboto Condensed",Arial,sans-serif;box-shadow:0 6px 8px rgba(0,0,0,.25);padding-top:14px}
.banner__title{font-family:"Open Sans",Arial,sans-serif;font-weight:800;font-size:21px;line-height:26px;letter-spacing:.2px}
.banner__title span{display:block;color:var(--yellow)}
.banner__cta{font-size:22px;margin-top:10px}
.banner__cta b{color:var(--yellow)}
.intro{position:absolute;left:14px;top:310px;width:320px;text-align:center;color:var(--muted);font-size:12px;line-height:16px}
.intro__address{font-weight:700;margin-top:8px;white-space:nowrap}
.referral{position:absolute;left:24px;top:427px;width:296px;height:39px;border-radius:10px;background:var(--blue);
  color:#fff;font-size:12px;padding:12px 0 0 9px;box-shadow:0 3px 5px rgba(0,0,0,.3)}
.tracks{position:absolute;left:330px;top:178px;width:307px;height:314px;background:var(--panel);padding:6px 0 0 17px}
.track__title{font-family:"Open Sans",Arial,sans-serif;font-weight:800;color:var(--red);font-size:13px;line-height:16px}
.track__title small{font-size:8px;color:var(--ink)}
.track{display:grid;grid-template-columns:74px 126px 1fr;font-size:8.3px;line-height:11.3px;margin-bottom:10px}
.track--manual{grid-template-columns:74px 98px 1fr;line-height:10.9px}
.track .gear{font-weight:800}

/* back */
.back-panel{position:absolute;left:0;top:0;width:440px;height:494px}
.banner--small{left:32px;top:17px;height:70px;width:290px;padding-top:8px}
.banner--small .banner__title{font-size:20px;line-height:26px}
.banner-fold{position:absolute;top:17px}
.letter{position:absolute;left:19px;top:97px;width:380px;font-size:9.4px;line-height:11.3px;text-align:justify}
.letter p{margin-bottom:11px}
.fields{position:absolute;left:17px;top:410px;width:340px;font-size:11px;line-height:17px;color:var(--muted)}
.contact{position:absolute;left:0;top:452px;width:440px;height:42px;color:#fff;font-size:11.2px;line-height:17px;text-align:center;white-space:nowrap}
.stamp{position:absolute;left:523px;top:28px;width:90px;height:54px;border:1.5px solid #9d9fa2}
</style>
</head>
<body>

<section class="card card--front">
  <div class="hero" role="img" aria-label="Photo of a blue SUV and a red SUV parked on grassland with a bare tree between them"></div>

  <div class="banner">
    <h1 class="banner__title">AUTOMATIC VS MANUAL<span>MONEY WAR</span></h1>
    <p class="banner__cta">Start engine: <b>$5 GET STARTED</b></p>
  </div>

  <div class="intro">
    <p>To qualify to recieve money on each track you just<br>need 4 people recruited or placed under you.<br>If you would like to receive money in this way,<br>send this card and $5 to:</p>
    <p class="intro__address">Carl Hendricks; 218 Elm St; Alder, WI 53900.</p>
  </div>

  <div class="referral">Referring Member_______________________________</div>

  <aside class="tracks">
    <h2 class="track__title">AUTOMATIC TRACK</h2>
    <div class="track">
      <span class="gear">1ST GEAR</span><span>$25 pays for 2nd gear</span><span>$25 pays you</span>
      <span class="gear">2ND GEAR</span><span>$75 pays for 3rd gear</span><span>$45 pays you</span>
      <span class="gear">3RD GEAR</span><span>$250 pays for 4th gear</span><span>$125 pays you</span>
      <span class="gear">4TH GEAR</span><span>$875 pays for 5th gear</span><span>$370 pays you</span>
      <span class="gear">5TH GEAR</span><span>$3125 pays for 6th gear</span><span>$1245 pays you</span>
      <span class="gear">6TH GEAR</span><span>$11,250 pays for 7th gear</span><span>$4370 pays you</span>
      <span class="gear">7TH GEAR</span><span>$40,625 pays for 8th gear</span><span>$15,620 pays you</span>
      <span class="gear">8TH GEAR</span><span>$146,875 pays for 9th gear</span><span>$56,245 pays you</span>
      <span class="gear">9TH GEAR</span><span>$5 pays for “Start Engine”</span><span>$734,365 pays you</span>
    </div>
    <h2 class="track__title">MANUAL TRACK <small>(5with 10 Plan)</small></h2>
    <div class="track track--manual">
      <span class="gear">1ST GEAR</span><span style="grid-column:2/4">$10 from “Start Engine” pays for 1st gear of 5with10.</span>
      <span class="gear">2ND GEAR</span><span>You pay $35</span><span>you receive $105</span>
      <span class="gear">3RD GEAR</span><span>You pay $60</span><span>you receive $210</span>
      <span class="gear">4TH GEAR</span><span>You pay $110</span><span>you receive $3460</span>
      <span class="gear">5TH GEAR</span><span>You pay $225</span><span>you receive $39,000</span>
      <span class="gear">6TH GEAR</span><span>You pay $100</span><span>you receive $3875</span>
      <span class="gear">7TH GEAR</span><span>You pay $430.00</span><span>you receive $78,000</span>
      <span class="gear">8TH GEAR</span><span>You pay $280</span><span>you receive $30,260</span>
      <span class="gear">9TH GEAR</span><span>You pay $200</span><span>you get $7,750</span>
      <span class="gear">10TH GEAR</span><span>You pay $2050</span><span>you get $390,000</span>
      <span class="gear">11TH GEAR</span><span>You pay $400</span><span>you get $15,500</span>
      <span class="gear">12TH GEAR</span><span>You pay $4100</span><span>you get $780,000</span>
    </div>
  </aside>
</section>

<section class="card card--back">
  <svg class="back-panel" viewBox="0 0 440 494" aria-hidden="true">
    <polygon points="0,40 350,40 410,448 0,448" fill="#e6e7e8"/>
    <polygon points="0,448 425,448 440,494 0,494" fill="#1e8fc4"/>
    <polygon points="410,441 425,448 410,448" fill="#156a92"/>
  </svg>
  <svg class="banner-fold" style="left:17px" width="15" height="16" viewBox="0 0 15 16" aria-hidden="true"><polygon points="15,0 15,16 0,16" fill="#7d1019"/></svg>
  <svg class="banner-fold" style="left:322px" width="15" height="16" viewBox="0 0 15 16" aria-hidden="true"><polygon points="0,0 0,16 15,16" fill="#7d1019"/></svg>

  <div class="banner banner--small">
    <h2 class="banner__title">AUTOMATIC VS MANUAL<span>MONEY WAR</span></h2>
  </div>

  <div class="letter">
    <p>Hello fellow income seeker,</p>
    <p>Like you I am looking for a product that will help me make money. Like you I also know that if I am working alone I may not be able to make the kind of money that I need to sustain me. That is why I am inviting you to join Automatic vs Manual Money War.</p>
    <p>If you are concerned about not being able to refer 2 people much less 4 then I have a solution for that. There are 3 different levels in which you can come in. The 3 levels are called Neutral, 2 Wheel Drive, and 4 Wheel Drive and are outlined below:</p>
    <p>Neutral: $5 you are entered into Auto VS Manual program and need 4 referrals to move into the 1st gear of both the Auto and Manual tracks.</p>
    <p>2 Wheel Drive: $15; $5 enters you into Auto VS Manual program; $10 enters you into the 1st gear of the Manual Track (5with10). You will receive 3 entries that will be eligible to go through the Auto Track. You will only need 2 referrals per entry to enter them into the Auto Track. After 6 referrals you will have 3 entries that are going through the Auto Track.</p>
    <p>4 Wheel Drive: $25; $5 enters you into Auto VS Manual program; $10 enters you into the 1st gear of the Manual Track (5with10); $10 enters one entry into the Auto Track. You will have 4 extra entries that will go through the Auto Track for a total of 5. Each entry will enter the Auto Track after 2 referrals per entry are placed below them.</p>
    <p>I hope that we can work together to become financially free.</p>
  </div>

  <div class="fields">
    <p>Name:________________________________________________</p>
    <p>Phone:__________________Email: ___________________________</p>
  </div>

  <div class="contact">
    <p>If you have any questions about how this Money War will play out feel free<br>to contact <b>Carl at 608-555-0148</b> or email him at <b>gearshift.club@example.com</b></p>
  </div>

  <div class="stamp" aria-label="Stamp area"></div>
</section>

</body>
</html>
```